Photography Studio Prep Guide Design Needed

I have a prep guide I send to all parents who book a session - It is outdated and ugly. I want a gorgeous, clean, modern upscale look for the brochure I send.

I already have the text and can provide photos for the final design. I want the cover to be clean and upscale and modern, with a happy feel.

Target Market(s)

My clients for an upscale Newborn Photography Studio

Requirements
Must have
• space for my photos, an upscale clean feel
Nice to have
• I love color, but don't want the brochure to look busy. I love cream, white, pale pink.

```html
<!DOCTYPE html>
<html lang="en">
<head>
<meta charset="utf-8">
<title>Parent Instructions &amp; Preparations</title>
<link href="https://fonts.googleapis.com/css2?family=Great+Vibes&family=Quicksand:wght@300;400&display=swap" rel="stylesheet">
<style>
  :root {
    --backdrop: #b9b8ba;
    --card: #e3c9e1;
    --title: #ffffff;
    --intro: #e2507f;
    --body: #a78ea8;
    --photo-deep: #6e2a5e;
    --photo-mid: #9c4a88;
    --photo-light: #d98ac0;
    --photo-centre: #c7a3d6;
  }
  html, body {
    margin: 0;
    width: 1200px;
    height: 1200px;
    overflow: hidden;
    background: var(--backdrop);
  }
  .guide-page {
    position: absolute;
    left: 51px;
    top: 162px;
    width: 1111px;
    height: 857px;
    background: var(--card);
    overflow: hidden;
    font-family: "Quicksand", sans-serif;
    font-weight: 300;
  }
  .page-title {
    position: absolute;
    left: 58px;
    top: 66px;
    margin: 0;
    font-family: "Great Vibes", cursive;
    font-weight: 400;
    font-size: 58px;
    line-height: 1;
    color: var(--title);
    white-space: nowrap;
  }
  .intro {
    position: absolute;
    left: 61px;
    top: 155px;
    margin: 0;
    font-size: 18.5px;
    line-height: 23.5px;
    color: var(--intro);
    letter-spacing: 0.3px;
    white-space: nowrap;
  }
  .section-heading {
    position: absolute;
    left: 58px;
    margin: 0;
    font-family: "Great Vibes", cursive;
    font-weight: 400;
    font-size: 30px;
    line-height: 1;
    color: var(--title);
  }
  .section-heading.nursing { top: 302px; }
  .section-heading.feeding { top: 674px; }
  .body-copy {
    position: absolute;
    margin: 0;
    font-size: 15px;
    line-height: 20.2px;
    letter-spacing: 0.2px;
    color: var(--body);
    white-space: nowrap;
  }
  .nursing-copy { left: 60px; top: 350px; }
  .feeding-copy { left: 60px; top: 727px; }
  .feeding-continued { left: 396px; top: 295px; }
  .session-photo {
    position: absolute;
    left: 559px;
    top: 177px;
    width: 530px;
    height: 530px;
    border-radius: 50%;
    background: radial-gradient(circle at 50% 50%, var(--photo-centre) 0%, #b98ac4 20%, var(--photo-deep) 38%, var(--photo-mid) 58%, var(--photo-light) 76%, var(--photo-mid) 90%, var(--photo-deep) 100%);
  }
</style>
</head>
<body>
  <main class="guide-page">
    <h1 class="page-title">Parent Instructions &amp; Preparations</h1>

    <p class="intro">
      Congratulations on expecting a baby!<br>
      Here are my instructions to ensure a successful<br>
      newborn photography session.<br>
      Please follow these instructions as closely as possible.
    </p>

    <div class="session-photo" role="img" aria-label="Newborn photo: sleeping baby wrapped in lilac in a nest surrounded by a ring of purple and pink flowers"></div>

    <h2 class="section-heading nursing">nursing</h2>
    <p class="body-copy nursing-copy">
      If you are nursing, please avoid eating<br>
      anything spicy (hot sauce, hot peppers,<br>
      curry, etc.) that might upset baby’s<br>
      tummy for 24 hours preceding your<br>
      scheduled session.<br>
      Please if you are breastfeeding do NOT<br>
      drink caffeine or coffee before your<br>
      session – I know this is hard but baby will<br>
      be wired if you have caffeine.<br>
      If you notice baby has a lot of gas<br>
      after feedings please check with your<br>
      pediatrician and bring gas drops<br>
      (Tummyease or other brand) to your session.<br>
      The most common reason a baby will<br>
      not settle for a session is gas pressure/<br>
      discomfort.
    </p>

    <h2 class="section-heading feeding">feeding</h2>
    <p class="body-copy feeding-copy">
      Feed the baby as much as possible in the<br>
      24 hours preceding your session – this will<br>
      help minimize the amount baby needs
    </p>

    <p class="body-copy feeding-continued">
      to feed during the<br>
      session, and will help<br>
      baby sleep as long<br>
      and as soundly<br>
      as possible.<br>
      Feed baby 2-3<br>
      hours before<br>
      your session and<br>
      not again until you<br>
      arrive. This feeding<br>
      is planned in your<br>
      session time and it’s<br>
      not rushed.<br>
      Please bring an extra<br>
      bottle of formula or<br>
      breastmilk to the session if<br>
      possible – sometimes a small<br>
      amount of milk in a bottle can<br>
      quickly soothe a baby back to sleep<br>
      without requiring a full feeding. I will<br>
      respect your wishes if you choose not<br>
      to use a bottle, but please understand we<br>
      may have to pass on some poses if baby<br>
      will not settle in position, and I cannot use<br>
      a bottle to soothe them into the pose.
    </p>
  </main>
</body>
</html>
```